Guaranteed Job - Sleek Sexy Business Card UV Spot

Im looking for a sleek and sexy business card, that resembles elite or VIP status status.
our business is corinvale.example
you can view our products on there, but our main audience for handing out our cards will be for people in the hospitality industry, so it will need to impress high management and CEO of hotels and restaurants, bars, clubs etc...
the card features will have UV spot on both sides, 400gsm stock. standard size.
Artwork should be 86 x 54mm + 2mm bleed = 90 x 58mm
it should have a nice "unique" uv spot pattern that highlights the card, not a repeated pattern, theres no originality there, and it will be disregarded.
The written material will be:
Corin Vale Hospitality College (logo)
Tobin Marsh
Director
Phone: 1300 615 737
Mobile: 0455 817 296
Email: info@corinvale.example
website: www.corinvale.example
I'm looking for originality here, i don't want just a simple stock card, want something that has a wow factor for people.
You will find the logo attached. you may invert the white to black words to suit the background as you please.
thank you and good luck
As a side note, ive received a lot of proposals, im too busy to give feedback to each and every one, so if i havent provided feedback for your design within 24 hours, then consider it not acceptable, and you could resubmit another design.
So far i have not seen any design that stood out for me, they all seem pretty generic. there nothing thats unique, i would figure for the amount that im offering, that people would put some more effort and creativity into the design.
so far over 200 designs submitted, and nothing i have seen looks very original, everything looks like a different variation of the same stuff, i said it very clearly i wanted something unique, the only thing that has come close to it so far is this one
Reason: Ive received alot of design concepts and i have reviewed everyone, but i havent had time to give feedback to every single one, only the ones that have interested me, if i havent responded, its because i havent found it good enough.
so far only a few design have been on par with what ive been looking for, an attractive eye popping design.
heres a few of them,
http://files.pixelbazaar.example/design_img/51736/62418/62418_2840915_51736_image.jpg
http://files.pixelbazaar.example/design_img/51736/68254/68254_2841377_51736_image.jpg
theyre, both unique and original, and eye catching, the only thing theyre missing is the sexyness.
if you still think you have some creativity left in your minds, then throw it on here.
Reason: Sorry guys for the delay, I was in a serious accident and out of commission for the past few months, I'm just slowly recovering now, please bare with me as i try to attend to this project, it may take me awhile as I have other projects that are on standby, I'm not 100% at the moment, so im extending the deadline for 2 weeks right now. Thanks for your patience.
Hospitality

```html
<!DOCTYPE html>
<html lang="en">
<head>
<meta charset="utf-8">
<title>Corin Vale Hospitality College – Business Card</title>
<link rel="stylesheet" href="https://fonts.googleapis.com/css2?family=Montserrat:wght@600;700&display=swap">
<style>
  :root {
    --backdrop: #3a3a3a;
    --card-black: #0e0e0e;
    --spot-grey: #5a5a5a;
    --spot-light: #c9c9c9;
    --card-blue-top: #3d9fdf;
    --card-blue-bottom: #1f86cf;
    --ink-white: #ffffff;
    --ink-deep-blue: #1456a8;
  }
  * { box-sizing: border-box; margin: 0; padding: 0; }
  html, body {
    width: 941px;
    height: 1200px;
    overflow: hidden;
    background: var(--backdrop);
    font-family: "Montserrat", Arial, sans-serif;
  }
  .canvas {
    position: relative;
    width: 941px;
    height: 1200px;
  }
  .card {
    position: absolute;
    left: 150px;
    width: 640px;
    height: 402px;
    border-radius: 4px;
    box-shadow: 0 10px 30px rgba(0, 0, 0, 0.45);
  }
  .card-front {
    top: 110px;
    background: var(--card-black);
  }
  .card-back {
    top: 690px;
    background: linear-gradient(160deg, var(--card-blue-top), var(--card-blue-bottom));
  }
  .brand {
    position: absolute;
    left: 70px;
    top: 150px;
    display: flex;
    align-items: center;
    gap: 22px;
  }
  .brand-square {
    width: 78px;
    height: 78px;
    background: var(--spot-grey);
  }
  .brand-name {
    color: var(--spot-light);
    font-weight: 700;
    font-size: 34px;
    line-height: 1.05;
    letter-spacing: 1px;
    text-transform: uppercase;
  }
  .brand-name .brand-sub {
    display: block;
    font-size: 17px;
    letter-spacing: 2px;
    margin-top: 4px;
  }
  .contact {
    position: absolute;
    right: 40px;
    top: 40px;
    text-align: right;
    color: var(--ink-white);
    font-weight: 700;
    text-transform: uppercase;
  }
  .contact-name {
    font-size: 44px;
    letter-spacing: 2px;
    line-height: 1.1;
  }
  .contact-role {
    font-size: 44px;
    letter-spacing: 2px;
    line-height: 1.1;
  }
  .contact-role .role-accent { color: var(--ink-deep-blue); }
  .contact-lines {
    margin-top: 48px;
    list-style: none;
  }
  .contact-line {
    display: flex;
    justify-content: flex-end;
    align-items: center;
    gap: 14px;
    font-size: 40px;
    letter-spacing: 3px;
    line-height: 1.15;
  }
  .contact-line svg { width: 26px; height: 26px; fill: var(--ink-deep-blue); }
  .contact-line .num-accent { color: var(--ink-deep-blue); }
  .contact-email {
    margin-top: 12px;
    font-size: 25px;
    letter-spacing: 1px;
    font-weight: 600;
    text-transform: none;
  }
</style>
</head>
<body>
<main class="canvas">
  <section class="card card-front" aria-label="Card front">
    <div class="brand">
      <span class="brand-square" aria-hidden="true"></span>
      <p class="brand-name">Corin Vale<span class="brand-sub">Hospitality College</span></p>
    </div>
  </section>

  <section class="card card-back" aria-label="Card back">
    <div class="contact">
      <p class="contact-name">Tobin Marsh</p>
      <p class="contact-role"><span class="role-accent">Di</span>rector</p>
      <ul class="contact-lines">
        <li class="contact-line">
          <svg viewBox="0 0 24 24" aria-label="Phone"><path d="M2 9c0-3 5-5 10-5s10 2 10 5v2h-5V9c-1-1-3-1.5-5-1.5S8 8 7 9v2H2z"/><rect x="5" y="12" width="14" height="8" rx="2"/></svg>
          <span><span class="num-accent">13</span>00 615 737</span>
        </li>
        <li class="contact-line">
          <svg viewBox="0 0 24 24" aria-label="Mobile"><rect x="6" y="2" width="12" height="20" rx="2"/><rect x="8" y="4" width="8" height="7" fill="#3d9fdf"/></svg>
          <span><span class="num-accent">04</span>55 817 296</span>
        </li>
      </ul>
      <p class="contact-email">info@corinvale.example</p>
    </div>
  </section>
</main>
</body>
</html>
```